TKVerdi Labels*

We are in the cannabis industry selling Cannabis products in a 1oz jar, 3oz jar and 7 oz jars. we have pre-rolls too.

We need various sizes logo label stickers for small jars and tubes. I need label sticker designs for some 1"x2", 2"x3", 2"x2" stickers logo. See attached for examples.

I'm attaching some samples for you to look at and see if you can design something in similar.

Attached is our Logo designed my ArtHive Project Design #: 58402937
Our Slogan is:

“Staying Passionate and motivated by high quality cannabis”

For any questions please do not hesitate to ask. Thank you

Target Market(s)

general comsumers

Industry/Entity Type

Cannabis

Font styles to use
Decorative

Colors
abd037
f36f22
f78f20
ffc41a

Requirements
Must have
• Warning: This product may be unlawful outside of the State of Washington. This soil grown product has intoxicating effects and my be habit forming. Smoking is hazardous to your health. There may be health risks associated with the consumption of this product. Marijuana can impair concentration, coordination and judgement. Do not operate a vehicle or machinery under the influence of this drug. Should not be use by women that are pregnant or breast feeding. For use only by adults twenty-one and older. Keep out reach of children.
Nice to have
• Small text box for cannabis name and strain type
• Marketing: Check Us Out!
• www.TKVerdiLLC-example.com
• TKVerdiLLC@mailnest-example.com
• Facebook TKVerdi LLC

```html
<!DOCTYPE html>
<html lang="en">
<head>
<meta charset="utf-8">
<title>TKVerdi 7 oz Jar Label</title>
<link rel="stylesheet" href="https://fonts.googleapis.com/css2?family=Montserrat:wght@400;500;600;700&display=swap">
<style>
  :root {
    --leaf-green: #abd037;
    --deep-green: #8cc43c;
    --lime: #d2e02a;
    --sun-yellow: #ffc41a;
    --label-white: #ffffff;
    --page-bg: #f4f4f2;
    --warning-text: #9cc43a;
  }
  html, body {
    margin: 0;
    width: 1093px;
    height: 1200px;
    overflow: hidden;
    background: var(--page-bg);
  }
  .jar-label {
    position: absolute;
    left: 40px;
    top: 266px;
    width: 1013px;
    height: 667px;
    display: block;
    font-family: "Montserrat", Arial, sans-serif;
  }
  .brand-name { fill: var(--warning-text); font-weight: 500; font-size: 17px; }
  .slogan { fill: var(--label-white); font-weight: 600; font-size: 15px; letter-spacing: 0.2px; }
  .warning-title { fill: var(--label-white); font-weight: 700; font-size: 10px; }
  .warning-copy { fill: var(--warning-text); font-weight: 400; font-size: 7.6px; }
  .strain-name { fill: var(--warning-text); font-weight: 700; font-size: 8px; }
  .net-weight { fill: var(--label-white); font-weight: 700; font-size: 8px; letter-spacing: 1px; }
</style>
</head>
<body>
<svg class="jar-label" viewBox="0 0 547 360" xmlns="http://www.w3.org/2000/svg" role="img" aria-label="TKVerdi 7 oz jar label">
  <defs>
    <linearGradient id="fieldGradient" x1="0" y1="0" x2="1" y2="0">
      <stop offset="0" stop-color="var(--lime)"/>
      <stop offset="1" stop-color="var(--deep-green)"/>
    </linearGradient>
  </defs>

  <!-- label base -->
  <rect class="label-base" x="0" y="0" width="547" height="360" fill="var(--label-white)"/>
  <rect class="top-trim" x="0" y="0" width="547" height="3" fill="var(--leaf-green)"/>

  <!-- brand pennant -->
  <polygon class="brand-pennant" points="215,0 330,0 330,100 272,118 215,100" fill="var(--label-white)" stroke="var(--leaf-green)" stroke-width="1"/>
  <circle class="brand-dot" cx="272" cy="46" r="13" fill="var(--leaf-green)"/>
  <text class="brand-name" x="272" y="84" text-anchor="middle">TKVerdi</text>

  <!-- roofline bands -->
  <polygon class="roof-yellow" points="0,190 280,112 547,196 547,335 0,335" fill="var(--sun-yellow)"/>
  <polygon class="roof-field" points="0,196 280,124 547,206 547,335 0,335" fill="url(#fieldGradient)"/>

  <!-- slogan -->
  <g class="slogan-block">
    <text class="slogan" x="256" y="193" text-anchor="middle">STAYING PASSIONATE</text>
    <text class="slogan" x="256" y="219" text-anchor="middle">AND</text>
    <text class="slogan" x="256" y="246" text-anchor="middle">MOTIVATED BY</text>
    <text class="slogan" x="256" y="272" text-anchor="middle">HIGH QUALITY</text>
    <text class="slogan" x="256" y="298" text-anchor="middle">CANNABIS</text>
  </g>

  <!-- footer band -->
  <rect class="footer-band" x="0" y="335" width="547" height="25" fill="var(--sun-yellow)"/>
  <text class="net-weight" x="272" y="351" text-anchor="middle">7 oz</text>

  <!-- warning panel -->
  <rect class="warning-box" x="396" y="20" width="134" height="214" fill="var(--label-white)" stroke="var(--sun-yellow)" stroke-width="2"/>
  <rect class="warning-tab" x="395" y="19" width="91" height="23" fill="var(--sun-yellow)"/>
  <text class="warning-title" x="404" y="35">WARNING:</text>
  <g class="warning-copy-block">
    <text class="warning-copy" x="403" y="58">This product may be</text>
    <text class="warning-copy" x="403" y="70">unlawful outside of the</text>
    <text class="warning-copy" x="403" y="82">State of Washington. This</text>
    <text class="warning-copy" x="403" y="94">soil grown product has</text>
    <text class="warning-copy" x="403" y="106">intoxicating effects and</text>
    <text class="warning-copy" x="403" y="118">my be habit forming.</text>
    <text class="warning-copy" x="403" y="130">Smoking is hazardous to</text>
    <text class="warning-copy" x="403" y="142">your health. There may be</text>
    <text class="warning-copy" x="403" y="154">health risks associated with</text>
    <text class="warning-copy" x="403" y="166">the consumption of this</text>
    <text class="warning-copy" x="403" y="178">product. Marijuana can</text>
    <text class="warning-copy" x="403" y="190">impair concentration,</text>
    <text class="warning-copy" x="403" y="202">coordination and</text>
    <text class="warning-copy" x="403" y="214">judgement.</text>
  </g>

  <!-- strain panel -->
  <rect class="strain-box" x="396" y="246" width="134" height="97" fill="var(--label-white)" stroke="var(--sun-yellow)" stroke-width="2"/>
  <text class="strain-name" x="463" y="303" text-anchor="middle">STRAIN NAME</text>
</svg>
</body>
</html>
```